Building company needs a letterhead design

I'm after a modern but professional letter head.
Must have the below details:
- Logo
- Website - TARVELGROUP.COM.AU
- Email - INFO@TARVELGROUP.COM.AU
- Office - 03 58206317
- Mobile number - 0413865290
- ABN - 47 318 264 105
...........................................................................................................................................................................................................................
- Logo
- Office - 03 58206317
- ABN - 47 318 264 105

Target Market(s)

.

Industry/Entity Type

Construction Company

Font styles to use
Sans Serif

Requirements
Must have
• Must have the below details:
• - Logo
• - Website - TARVELGROUP.COM.AU
• - Email - INFO@TARVELGROUP.COM.AU
• - Office - 03 58206317
• - Mobile number - 0413865290
• - ABN - 47 318 264 105
Nice to have
• .
Should not have
• .

```html
<!DOCTYPE html>
<html lang="en">
<head>
<meta charset="utf-8">
<title>Tarvel Building Group Letterhead</title>
<link href="https://fonts.googleapis.com/css2?family=Open+Sans:wght@400;600;700;800&display=swap" rel="stylesheet">
<style>
  :root {
    --backdrop: #e9e9ea;
    --paper: #ffffff;
    --brand-amber: #e5a400;
    --brand-charcoal: #575455;
    --ink: #4a4a4a;
    --ink-dark: #1f1f1f;
  }
  html, body {
    margin: 0;
    width: 1200px;
    height: 1192px;
    overflow: hidden;
    background: var(--backdrop);
    font-family: "Open Sans", Arial, sans-serif;
  }
  .letterhead {
    position: absolute;
    left: 210px;
    top: 46px;
    width: 780px;
    height: 1100px;
    background: var(--paper);
    box-shadow: 0 2px 10px rgba(0,0,0,0.08);
    overflow: hidden;
  }
  .brand {
    position: absolute;
    left: 72px;
    top: 72px;
    display: flex;
    align-items: center;
    gap: 10px;
  }
  .brand-mark {
    width: 30px;
    height: 30px;
    background: var(--brand-amber);
  }
  .brand-name {
    font-weight: 800;
    font-size: 17px;
    letter-spacing: 0.5px;
    line-height: 1.1;
    color: var(--brand-amber);
    margin: 0;
  }
  .contact {
    position: absolute;
    right: 60px;
    top: 230px;
    margin: 0;
    padding: 0;
    list-style: none;
    font-size: 10.5px;
    line-height: 15px;
    color: var(--ink);
  }
  .contact li {
    display: flex;
    align-items: center;
    gap: 8px;
  }
  .contact svg {
    width: 9px;
    height: 9px;
    fill: var(--brand-amber);
    flex: none;
  }
  .footer-swoosh {
    position: absolute;
    left: 0;
    bottom: 0;
    width: 780px;
    height: 300px;
  }
  .abn {
    position: absolute;
    right: 70px;
    bottom: 42px;
    margin: 0;
    font-size: 12px;
    font-weight: 700;
    color: var(--ink-dark);
  }
</style>
</head>
<body>
  <main class="letterhead">
    <header class="brand">
      <span class="brand-mark"></span>
      <p class="brand-name">TARVEL<br>BUILDING GROUP</p>
    </header>

    <ul class="contact">
      <li>
        <svg viewBox="0 0 10 10"><path d="M2 0.5 L3.8 2.6 L2.9 3.6 Q4 5.9 6.4 7.1 L7.4 6.2 L9.5 8 L8.3 9.5 Q1 8 0.5 1.7 Z"/></svg>
        03 58206317
      </li>
      <li>
        <svg viewBox="0 0 10 10"><rect x="2.5" y="0" width="5" height="10" rx="1"/><rect x="3.4" y="1.2" width="3.2" height="6" fill="#fff"/></svg>
        0413865290
      </li>
      <li>
        <svg viewBox="0 0 10 10"><rect x="0" y="1.5" width="10" height="7" rx="1"/><path d="M0.5 2 L5 5.5 L9.5 2" stroke="#fff" stroke-width="1" fill="none"/></svg>
        info@tarvelgroup.com.au
      </li>
      <li>
        <svg viewBox="0 0 10 10"><circle cx="5" cy="5" r="4.5"/><path d="M0.5 5 H9.5 M5 0.5 Q2.5 5 5 9.5 M5 0.5 Q7.5 5 5 9.5" stroke="#fff" stroke-width="0.8" fill="none"/></svg>
        www.tarvelgroup.com.au
      </li>
    </ul>

    <svg class="footer-swoosh" viewBox="0 0 780 300" aria-hidden="true">
      <path fill="var(--brand-amber)" d="M0 40 Q420 150 780 175 L780 300 L0 300 Z"/>
      <path fill="var(--brand-charcoal)" d="M220 70 Q520 115 780 118 L780 158 Q470 130 220 70 Z"/>
    </svg>

    <p class="abn">ABN - 47 318 264 105</p>
  </main>
</body>
</html>
```